Fahrzeugbeschriftung für Gebäudetechnik (Heizung/Sanitär, Elektrotechnik, Klimatechnik)
Zielgruppe
Wir sind eine Werbeagentur mit Schwerpunkt Personalmarketing und brauchen für einen Kunden ein Autodesign für verschiedene Modelle. Der Kunde ist ein Unternehmen im Bereich Gebäudetechnik (Heizung/Sanitär, Elektrotechnik, Klimatechnik).
Aufgabenstellung
Logo, Telefonnummer und eine kurze Leistungsübersicht (Heizung/Sanitär, Elektrotechnik, Klimatechnik).
Designfarben sollen dem CI entsprechen siehe http://www.tkvbremlor.example/ (Webseite ist noch im Aufbau).
Trotzdem soll es etwas auffälliges sein.
Unbedingt bisschen Platz freilassen für extra Aufkleber!
Design sollte für folgende oder ähnliche Modelle passen:
1. Varko Lastmo Prime 420K Series
2. Ostra Kastenwagen L2H2
3. Ostra Kastenwagen L1H1

```html
<!DOCTYPE html>
<html lang="de">
<head>
<meta charset="utf-8">
<title>Tekvaro – Fahrzeugbeschriftung</title>
<link rel="stylesheet" href="https://fonts.googleapis.com/css2?family=Open+Sans:wght@600;700&display=swap">
<style>
:root{
  --brand-cyan:#16aecb;
  --brand-navy:#1e3a56;
  --wave-light:#cfeaf0;
  --wave-mid:#a9dbe6;
  --panel-line:#d6dbe0;
  --paper:#ffffff;
  --lettering-tone:#dfeff3;
}
*{box-sizing:border-box;margin:0;padding:0}
html,body{width:1200px;height:790px;overflow:hidden;background:var(--paper)}
.canvas{position:relative;width:1200px;height:790px;font-family:"Open Sans",sans-serif;color:var(--brand-navy)}
.view{position:absolute;background:var(--paper);border:1px solid var(--panel-line);border-radius:18px;overflow:hidden}
.view-front{left:110px;top:110px;width:280px;height:230px}
.view-side-right{left:495px;top:112px;width:590px;height:228px}
.view-rear{left:115px;top:425px;width:255px;height:250px}
.view-side-left{left:470px;top:445px;width:590px;height:230px}
.wave{position:absolute;inset:0;width:100%;height:100%}
.brand{position:absolute;display:flex;align-items:center;gap:8px;white-space:nowrap}
.brand-mark{flex:none;background:var(--brand-cyan)}
.brand-name{font-family:"Open Sans",sans-serif;font-weight:700;color:var(--brand-cyan);line-height:1}
.brand-lg .brand-name{font-size:46px}
.brand-lg .brand-mark{width:16px;height:16px}
.brand-md .brand-name{font-size:26px}
.brand-md .brand-mark{width:10px;height:10px}
.brand-md{gap:6px}
.brand-sm .brand-name{font-size:17px}
.brand-sm .brand-mark{width:7px;height:7px}
.brand-sm{gap:4px}
.service-list{position:absolute;font-weight:700;text-transform:uppercase;line-height:1.25;white-space:nowrap}
.service-list-sm{font-size:5.5px}
.service-list-md{font-size:8px}
.hiring-lettering{position:absolute;background:var(--lettering-tone);border-radius:8px}
.service{position:absolute;display:flex;align-items:center;gap:5px;font-size:7.5px;font-weight:700;text-transform:uppercase;white-space:nowrap}
.service-icon{width:19px;height:19px}
.contact{position:absolute;font-weight:700;line-height:1.35;white-space:nowrap}
.contact-line{display:flex;align-items:center;gap:4px}
.contact-phone{font-size:10.5px}
.contact-web{font-size:8px}
.contact-rear .contact-phone{font-size:11px}
.contact-rear .contact-web{font-size:8.5px}
.contact-icon{width:9px;height:9px;flex:none}
.door-seam{position:absolute;top:0;bottom:0;width:1px;background:var(--panel-line)}
</style>
</head>
<body>
<div class="canvas">

  <section class="view view-front" aria-label="Frontansicht">
    <div class="brand brand-sm" style="left:72px;top:104px">
      <span class="brand-mark"></span><span class="brand-name">Tekvaro</span>
    </div>
    <div class="service-list service-list-sm" style="left:158px;top:103px">Heizung + Sanitär<br>Elektrik<br>Klimatechnik</div>
  </section>

  <section class="view view-side-right" aria-label="Seitenansicht rechts">
    <svg class="wave" viewBox="0 0 590 228" preserveAspectRatio="none" aria-hidden="true">
      <path d="M0 120 C80 95 200 100 300 160 C340 185 360 210 370 228 L0 228Z" fill="var(--wave-light)"/>
      <path d="M120 228 C160 170 260 160 330 190 C350 200 360 215 365 228Z" fill="var(--wave-mid)" opacity=".7"/>
    </svg>
    <div class="hiring-lettering" role="img" aria-label="Handschrift: Unser Team wächst. Bewirb dich bei uns!" style="left:40px;top:20px;width:100px;height:58px"></div>
    <div class="brand brand-lg" style="left:160px;top:26px">
      <span class="brand-mark"></span><span class="brand-name">Tekvaro</span>
    </div>
    <div class="service" style="left:20px;top:112px">Elektrotechnik
      <svg class="service-icon" viewBox="0 0 20 20"><circle cx="10" cy="10" r="10" fill="var(--brand-cyan)"/><path d="M11 3 L6 11 H9.5 L8.5 17 L14 8.5 H10.5Z" fill="#fff"/></svg></div>
    <div class="service" style="left:118px;top:114px">Klimatechnik
      <svg class="service-icon" viewBox="0 0 20 20"><circle cx="10" cy="10" r="10" fill="var(--brand-cyan)"/><g stroke="#fff" stroke-width="1.5" stroke-linecap="round"><path d="M10 4v12M4.8 7l10.4 6M4.8 13l10.4-6"/></g></svg></div>
    <div class="service" style="left:210px;top:116px">Heizung+Sanitär
      <svg class="service-icon" viewBox="0 0 20 20"><circle cx="10" cy="10" r="10" fill="var(--brand-cyan)"/><g fill="#fff"><rect x="5" y="6" width="1.6" height="8" rx=".8"/><rect x="8" y="6" width="1.6" height="8" rx=".8"/><rect x="11" y="6" width="1.6" height="8" rx=".8"/><rect x="14" y="6" width="1.6" height="8" rx=".8"/></g></svg></div>
    <div class="contact" style="left:342px;top:114px">
      <div class="contact-line contact-phone"><svg class="contact-icon" viewBox="0 0 10 10"><path d="M2 1 L4 1 L4.6 3 L3.4 4 C4 5.4 4.8 6.2 6 6.6 L7 5.4 L9 6 L9 8 C9 8.6 8.6 9 8 9 C4.2 9 1 5.8 1 2 C1 1.4 1.4 1 2 1Z" fill="var(--brand-navy)"/></svg>040 555 01 234</div>
      <div class="contact-line contact-web"><svg class="contact-icon" viewBox="0 0 10 10"><g fill="none" stroke="var(--brand-navy)" stroke-width="1"><circle cx="5" cy="5" r="4"/><ellipse cx="5" cy="5" rx="1.8" ry="4"/><path d="M1 5h8"/></g></svg>tkvbremlor.example</div>
    </div>
  </section>

  <section class="view view-rear" aria-label="Heckansicht">
    <svg class="wave" viewBox="0 0 255 250" preserveAspectRatio="none" aria-hidden="true">
      <path d="M255 95 C190 95 150 150 135 250 L255 250Z" fill="var(--wave-light)"/>
      <path d="M255 150 C200 160 180 210 175 250 L255 250Z" fill="var(--wave-mid)" opacity=".6"/>
    </svg>
    <span class="door-seam" style="left:127px"></span>
    <div class="brand brand-md" style="left:30px;top:42px">
      <span class="brand-mark"></span><span class="brand-name">Tekvaro</span>
    </div>
    <div class="service-list service-list-md" style="left:133px;top:76px">Heizung + Sanitär<br>Elektrik<br>Klimatechnik</div>
    <div class="hiring-lettering" role="img" aria-label="Handschrift: Unser Team wächst. Bewirb dich bei uns!" style="left:30px;top:108px;width:84px;height:46px"></div>
    <div class="contact contact-rear" style="left:133px;top:130px">
      <div class="contact-line contact-phone"><svg class="contact-icon" viewBox="0 0 10 10"><path d="M2 1 L4 1 L4.6 3 L3.4 4 C4 5.4 4.8 6.2 6 6.6 L7 5.4 L9 6 L9 8 C9 8.6 8.6 9 8 9 C4.2 9 1 5.8 1 2 C1 1.4 1.4 1 2 1Z" fill="var(--brand-navy)"/></svg>040 555 01 234</div>
      <div class="contact-line contact-web"><svg class="contact-icon" viewBox="0 0 10 10"><g fill="none" stroke="var(--brand-navy)" stroke-width="1"><circle cx="5" cy="5" r="4"/><ellipse cx="5" cy="5" rx="1.8" ry="4"/><path d="M1 5h8"/></g></svg>tkvbremlor.example</div>
    </div>
  </section>

  <section class="view view-side-left" aria-label="Seitenansicht links">
    <svg class="wave" viewBox="0 0 590 230" preserveAspectRatio="none" aria-hidden="true">
      <path d="M590 95 C480 90 330 110 270 180 C255 200 250 215 250 230 L590 230Z" fill="var(--wave-light)"/>
      <path d="M590 150 C500 150 420 180 400 230 L590 230Z" fill="var(--wave-mid)" opacity=".6"/>
    </svg>
    <div class="brand brand-lg" style="left:245px;top:28px">
      <span class="brand-mark"></span><span class="brand-name">Tekvaro</span>
    </div>
    <div class="hiring-lettering" role="img" aria-label="Handschrift: Unser Team wächst. Bewirb dich bei uns!" style="left:462px;top:22px;width:100px;height:58px"></div>
    <div class="contact" style="left:160px;top:120px">
      <div class="contact-line contact-phone"><svg class="contact-icon" viewBox="0 0 10 10"><path d="M2 1 L4 1 L4.6 3 L3.4 4 C4 5.4 4.8 6.2 6 6.6 L7 5.4 L9 6 L9 8 C9 8.6 8.6 9 8 9 C4.2 9 1 5.8 1 2 C1 1.4 1.4 1 2 1Z" fill="var(--brand-navy)"/></svg>040 555 01 234</div>
      <div class="contact-line contact-web"><svg class="contact-icon" viewBox="0 0 10 10"><g fill="none" stroke="var(--brand-navy)" stroke-width="1"><circle cx="5" cy="5" r="4"/><ellipse cx="5" cy="5" rx="1.8" ry="4"/><path d="M1 5h8"/></g></svg>tkvbremlor.example</div>
    </div>
    <div class="service" style="left:283px;top:120px">
      <svg class="service-icon" viewBox="0 0 20 20"><circle cx="10" cy="10" r="10" fill="var(--brand-cyan)"/><g fill="#fff"><rect x="5" y="6" width="1.6" height="8" rx=".8"/><rect x="8" y="6" width="1.6" height="8" rx=".8"/><rect x="11" y="6" width="1.6" height="8" rx=".8"/><rect x="14" y="6" width="1.6" height="8" rx=".8"/></g></svg>Heizung+Sanitär</div>
    <div class="service" style="left:383px;top:116px">
      <svg class="service-icon" viewBox="0 0 20 20"><circle cx="10" cy="10" r="10" fill="var(--brand-cyan)"/><g stroke="#fff" stroke-width="1.5" stroke-linecap="round"><path d="M10 4v12M4.8 7l10.4 6M4.8 13l10.4-6"/></g></svg>Klimatechnik</div>
    <div class="service" style="left:472px;top:112px">
      <svg class="service-icon" viewBox="0 0 20 20"><circle cx="10" cy="10" r="10" fill="var(--brand-cyan)"/><path d="M11 3 L6 11 H9.5 L8.5 17 L14 8.5 H10.5Z" fill="#fff"/></svg>Elektrotechnik</div>
  </section>

</div>
</body>
</html>
```